"The Summit Hour Audio Series" needs 3 banner ad designs

I am seeking the design and creation of 3 differently-designed ”banner ads.” I want them to look as though there is a relation between designs but I don't want them to look the same.
While compatibility is desired, that desire should not be interpreted as sameness.

I need a series of banner ads to be a supplement and a complement to
"The Summit Hour"'s main banner ad page and accompanying site.
http://www.quorvale.org/

I am looking for high quality, creative capturing of banner ads that focus on three topic areas, namely, my:

1. Leadership Coaching Program –
“Stride Builder Mentoring Track™”

2. Training program – “The Craft of a Steady Captain”

and

3. Speaker Interest & Availability banner ad.

It is desired that each banner, and the banners collectively, complement and fit in with the look and feel of the existing, principal banner and the show’s vision and mission. (in the attachment, I have included a copy of this banner for your information).

The final design should commit experience, competence, depth and reliability.

To provide a bit of context for this request, I have included the show's vision and mission statement as well as a brief description of my perspective on each banner ad.

I will of course, provide the winner all of the information, documents, graphic depictions, etc that I have available (during the handover stage) that will enable them to create quality products.

In addition, each banner ad should be delivered as JPEG files in dimensions 728 pixel wide and 90 pixels high each. The following fonts: Veltrane Serif Regular or Thomas Condensed Regular are the desired fonts.

The task summary: Design 3 banner ads as described below:

1. Leadership Coaching Program – Stride Builder Mentoring Track™
My coaching program has a formal structure that has an existing graphic capturing of leadership coaching that that would/should be incorporated in the ad.

2. Training program – The Craft of a Steady Captain
The skills training program description I have included as noted below; it is a program that can also be licensed for use by customers who would wish to use it in their organization. In addition to the creative thinking of graphics artists, it would probably be useful to view the home page graphic at www.tovrik4.com. This image might be useful in enhancing the banner ad graphic.

3. Speaking Interest – Availability
Have been and desire using this banner to communicate my interest in generating value and availability as a speaker.

-Vision-
“The Summit Hour”
Making an Impact through Effective Leadership
*is a powerfully engaging platform for great conversations about leadership and leadership learning.

-Mission-
Build a community of listeners who are informed and enthusiastically engaged with the host and the show’s goal of improving the quality of leadership wherever listeners are living and leading.

File: "1785 Postcard V2" - *this information is for use in designing the
Leadership Coaching Banner Ad* = *Stride Builder Mentoring Track*

File: "Cover Shot of Skills Book" - *this information is
for use in designing the Book Ad – The Craft of a Steady Captain:
Growing a Guide Whom Peers Gladly Trust*

File: (word doc) The Craft of a Steady Captain Training Workshop – Skills &
Concepts Summary *this information is for the design of the banner ad for
the Skills Training Course. It includes quotes that could be excerpted to
include in the banner ad*

File name: "Cover - Craft of a Steady Captain"
-> Picture of book for Craft of a Steady Captain Training Program – *this is additional information for the use in designing the Training program banner ad

You can find the other attachments useful. Please have a look.
I welcome all your creative and original designs. Remember, these are 3 different-looking banner ads - though related in some way.

Project Deadline Extended Reason: The current designs have not included enough variety and creativity. While I am desirous of compatibility of the ad renditions with the central image, I am not interpreting compatibility with sameness of looking to see the same image in each banner ad. I rather think the image differentiation promotes both interest and distinction between the products of book, leadership coaching, speaking, etc. Same image embedded in each banner ad doesn't provide the variety that I think both distinguishes and draws interest. In this regard, most of the current examples include the same pictorial images across designs and the use of just words vs. images from among those provided, As an example a picture of my book on the book banner ad seems more impactful than merely using the words book on the ad for the book; and the picture of a speaker vs. Speaker Availability.I hope this feedback is helpful . Regards,Leopold Added Saturday, June 3, 2017

Target Market(s)

Online Radio Listeners Can Visit WavelineHub.com for examples - Will be broadcast on the Commerce Channel

Industry/Entity Type

Business Consultant

Colors

Designer to choose colors to be used in the design.

Requirements
Should not have
• Anything that doesn't speak to the characteristics noted at the end of the summary provided in the description above

```html
<!DOCTYPE html>
<html lang="en">
<head>
<meta charset="utf-8">
<title>The Summit Hour Audio Series – Banner Ads</title>
<link rel="stylesheet" href="https://fonts.googleapis.com/css2?family=Barlow:wght@600&family=Cinzel:wght@400&display=swap">
<style>
  :root {
    --sheet-top: #ffffff;
    --sheet-bottom: #f0f0f2;
    --spec-grey: #8a8a8a;
    --label-grey: #7d7d7d;
    --banner-black: #000000;
    --banner-text: #f4f1ea;
    --concrete-dark: #2a2a2a;
    --concrete-mid: #4a4744;
    --warm-glow: #e9d9a6;
    --sunset: #b98a4a;
  }
  * { margin: 0; padding: 0; box-sizing: border-box; }
  html, body { width: 1200px; height: 1200px; overflow: hidden; }
  body {
    position: relative;
    background: linear-gradient(to bottom, var(--sheet-top) 0, var(--sheet-top) 628px, var(--sheet-bottom) 628px);
    font-family: "Barlow", Arial, sans-serif;
  }
  .spec-sheet {
    position: absolute; left: 56px; top: 48px;
    color: var(--spec-grey); font-weight: 600; font-size: 20px; line-height: 29px;
  }
  .banner-label {
    position: absolute; left: 53px;
    color: var(--label-grey); font-weight: 600; font-size: 15px;
  }
  .banner {
    position: absolute; left: 48px; width: 1104px; height: 136px;
    background: var(--banner-black); overflow: hidden;
  }
  .banner-title {
    position: absolute; font-family: "Cinzel", "Times New Roman", serif;
    color: var(--banner-text); font-weight: 400; white-space: nowrap; letter-spacing: 0.04em;
  }
  .photo { position: absolute; top: 0; height: 100%; }

  /* Banner 1 */
  .banner--coaching { top: 162px; }
  .banner--coaching .photo {
    left: 700px; width: 404px;
    background:
      radial-gradient(ellipse 60px 70px at 330px 50px, var(--warm-glow) 0%, rgba(233,217,166,0.5) 45%, transparent 75%),
      linear-gradient(to right, var(--banner-black) 0%, var(--concrete-dark) 30%, var(--concrete-mid) 70%, #6a625a 100%);
  }
  .banner--coaching .line-one { left: 56px; top: 38px; font-size: 23px; }
  .banner--coaching .line-two { left: 56px; top: 70px; font-size: 30px; }
  .banner--coaching sup { font-size: 9px; vertical-align: top; }

  /* Banner 2 */
  .banner--training { top: 343px; }
  .banner--training .photo {
    left: 0; width: 300px;
    background:
      radial-gradient(ellipse 110px 60px at 140px 100px, rgba(233,200,140,0.85) 0%, rgba(185,138,74,0.4) 50%, transparent 80%),
      linear-gradient(to right, #2b2620 0%, #3a342c 60%, var(--banner-black) 100%);
  }
  .banner--training .line-one { left: 344px; top: 34px; font-size: 26px; }
  .banner--training .line-two { left: 344px; top: 68px; font-size: 38px; }

  /* Banner 3 */
  .banner--speaker { top: 527px; }
  .banner--speaker .photo {
    left: 720px; width: 384px;
    background:
      radial-gradient(ellipse 110px 60px at 200px 60px, rgba(240,240,240,0.55) 0%, rgba(120,120,120,0.3) 50%, transparent 80%),
      linear-gradient(to right, var(--banner-black) 0%, #262626 40%, #3a3a3a 100%);
  }
  .banner--speaker .line-one { left: 122px; top: 47px; font-size: 35px; }
</style>
</head>
<body>
  <div class="spec-sheet">
    <p>728px x 90px &nbsp;|&nbsp; Fonts: Veltrane Serif Regular &nbsp;&nbsp;|&nbsp; JPG</p>
    <p>Images should buy from PICTAVERN</p>
  </div>

  <p class="banner-label" style="top:141px">Banner Ad 1</p>
  <section class="banner banner--coaching">
    <div class="photo" role="img" aria-label="Concrete wall with stone steps, an arrow and a glowing light bulb holding a businessman silhouette"></div>
    <h2 class="banner-title line-one">Leadership Coaching Program –</h2>
    <h2 class="banner-title line-two">Stride Builder Mentoring Track<sup>™</sup></h2>
  </section>

  <p class="banner-label" style="top:322px">Banner Ad 2</p>
  <section class="banner banner--training">
    <div class="photo" role="img" aria-label="Rising bar columns glowing with a city sunset and a businessman walking toward them"></div>
    <h2 class="banner-title line-one">Training program –</h2>
    <h2 class="banner-title line-two">The Craft of a Steady Captain</h2>
  </section>

  <p class="banner-label" style="top:506px">Banner Ad 3</p>
  <section class="banner banner--speaker">
    <div class="photo" role="img" aria-label="Open hand holding a glowing cloud of hand-drawn idea and plan sketches"></div>
    <h2 class="banner-title line-one">Speaker Interest &amp; Availability</h2>
  </section>
</body>
</html>
```